DL flyer for boat tour business in Sydney

I need a DL flyer (99mmx210mm) for my boat tour business 'Roam Coral Bayline'. For the text on the flyer please see the PDF template provided. The template is just a suggestion and I am open to any other designs, different fonts and colors. Please have a look at my company website www.roamcoralbayline.com.au to get a better understanding of the business.

Target Market(s)

Tourists and locals in Sydney. Generally the target customers are active, stylish, adventurous and want a custom, upscale experience.

Industry/Entity Type

Tourism

Font styles to use
Sans Serif

Colors
0355a3
3276b5
ec1f27
f04a50
85cae6
34a6d7

Requirements
Must have
• See template as suggestion.

```html
<!DOCTYPE html>
<html lang="en">
<head>
<meta charset="utf-8">
<title>Roam Coral Bayline – DL Flyer</title>
<link href="https://fonts.googleapis.com/css2?family=Questrial&family=Montserrat:wght@600&display=swap" rel="stylesheet">
<style>
  :root {
    --backdrop: #a4dfd6;
    --paper: #efefef;
    --navy: #0355a3;
    --blue: #3276b5;
    --red: #ec1f27;
    --red-soft: #f04a50;
    --sky: #85cae6;
    --sea: #34a6d7;
    --lime: #9dcc4c;
    --ink: #1c1c1c;
  }
  * { margin: 0; padding: 0; box-sizing: border-box; }
  html, body { width: 1200px; height: 900px; overflow: hidden; }
  body {
    background: var(--backdrop);
    font-family: "Questrial", sans-serif;
    color: var(--ink);
    position: relative;
  }
  .flyer {
    position: absolute;
    top: 40px;
    left: 130px;
    width: 940px;
    height: 820px;
    display: flex;
  }
  .panel {
    position: relative;
    width: 470px;
    height: 820px;
    background: var(--paper);
    overflow: hidden;
  }
  .panel + .panel { border-left: 1px solid #dcdcdc; }

  .masthead {
    position: absolute;
    top: 0; left: 0; right: 0;
    height: 92px;
    display: flex;
    align-items: center;
    padding: 0 22px;
    gap: 12px;
    z-index: 2;
  }
  .brand-dot {
    width: 40px; height: 40px;
    border-radius: 50%;
    background: var(--sea);
    flex: none;
  }
  .brand-name {
    font-family: "Questrial", sans-serif;
    font-size: 25px;
    color: var(--navy);
    letter-spacing: 0.5px;
    text-transform: uppercase;
    white-space: nowrap;
  }

  .hero-photo {
    position: absolute;
    top: 0; left: 0;
    width: 470px; height: 323px;
    background: linear-gradient(180deg, #7fb9e6 0%, #cfe6f4 30%, #d8d6cf 48%, #3aa3b6 62%, #1f7f96 100%);
  }
  .hero-photo::after {
    content: "";
    position: absolute;
    left: 0; right: 0; top: 0;
    height: 92px;
    background: linear-gradient(180deg, rgba(255,255,255,.85), rgba(255,255,255,0));
  }

  .headline-block {
    position: absolute;
    top: 323px; left: 0;
    width: 470px; height: 245px;
    background: var(--lime);
    padding: 20px 36px 0 36px;
  }
  .headline {
    font-family: "Montserrat", sans-serif;
    font-weight: 600;
    font-size: 50px;
    line-height: 50px;
    color: var(--ink);
    text-transform: uppercase;
    letter-spacing: -0.5px;
  }
  .headline-sub {
    margin-top: 14px;
    font-size: 17px;
    line-height: 19px;
    width: 350px;
  }

  .note {
    position: absolute;
    top: 598px; left: 42px;
    font-size: 17px;
    line-height: 18px;
  }
  .note strong {
    display: block;
    font-size: 21px;
    font-weight: 400;
    letter-spacing: -0.3px;
    -webkit-text-stroke: 0.4px var(--ink);
  }

  .sign-off {
    position: absolute;
    left: 0; right: 0;
    bottom: 22px;
    text-align: center;
  }
  .sign-off .brand-mini {
    display: inline-flex;
    align-items: center;
    gap: 8px;
    margin-bottom: 18px;
  }
  .sign-off .brand-mini .brand-dot { width: 30px; height: 30px; }
  .sign-off .brand-mini .brand-name { font-size: 15px; color: var(--navy); }
  .book-now {
    font-size: 19px;
    color: var(--red);
    line-height: 22px;
  }
  .web-address {
    font-size: 17px;
    letter-spacing: 1px;
    text-transform: uppercase;
    line-height: 22px;
  }

  .route-map {
    position: absolute;
    top: 96px; left: 0;
    width: 470px; height: 242px;
    background: linear-gradient(120deg, #e9e6df 0%, #b9cde8 45%, #c7d7ee 70%, #e6e3dc 100%);
  }

  .section {
    position: absolute;
    left: 30px;
    width: 340px;
  }
  .section-title {
    font-family: "Montserrat", sans-serif;
    font-weight: 600;
    font-size: 22px;
    color: var(--navy);
    text-transform: uppercase;
    margin-bottom: 6px;
  }
  .section p {
    font-size: 16px;
    line-height: 18.5px;
  }
  .experience { top: 360px; }
  .directions { top: 536px; }
</style>
</head>
<body>
  <main class="flyer">
    <section class="panel panel-front">
      <div class="hero-photo" role="img" aria-label="Photo of a red speedboat on the harbour with the opera house and harbour bridge behind"></div>
      <header class="masthead">
        <span class="brand-dot"></span>
        <span class="brand-name">Roam Coral Bayline</span>
      </header>
      <div class="headline-block">
        <h1 class="headline">Captain<br>your<br>own boat!</h1>
        <p class="headline-sub">Experience the major highlights of the most beautiful harbour in the world while driving your own boat.</p>
      </div>
      <p class="note"><strong>No boating</strong>Experience or boat license required.</p>
      <footer class="sign-off">
        <div class="brand-mini"><span class="brand-dot"></span><span class="brand-name">Roam Coral Bayline</span></div>
        <p class="book-now">Book Now Online!</p>
        <p class="web-address">www.roamcoralbayline.com.au</p>
      </footer>
    </section>

    <section class="panel panel-back">
      <header class="masthead">
        <span class="brand-dot"></span>
        <span class="brand-name">Roam Coral Bayline</span>
      </header>
      <div class="route-map" role="img" aria-label="Map of the harbour showing the tour route traced in red"></div>
      <div class="section experience">
        <h2 class="section-title">The Experience</h2>
        <p>Roam Coral Bayline offers guided 2 hour self-drive tours in small groups to the major highlights in the harbour. Follow our knowledgeable and experienced guides for a very personal tour.</p>
      </div>
      <div class="section directions">
        <h2 class="section-title">Directions</h2>
        <p>Our tours start from the Kelpie Point Boat ramp, which can be easily reached by car, buses 411, 412 and 415, as well as the K3 Bayline Ferry.</p>
      </div>
      <footer class="sign-off">
        <div class="brand-mini"><span class="brand-dot"></span><span class="brand-name">Roam Coral Bayline</span></div>
        <p class="book-now">Book Now Online!</p>
        <p class="web-address">www.roamcoralbayline.com.au</p>
      </footer>
    </section>
  </main>
</body>
</html>
```